Sanding Disc Box Packaging Graphic design

We need a package design for 5" hook and loop sanding discs designed for use with random orbital sanders.

The Brand name is "BADGER BITE". Our brand stands for Quality, Strength and durability at an affordable price.
Sanding discs packaging, and tool packaging tends to be very functional and straightforward. We are looking for a package design that is creative and stands out while maintaining a serious and professional quality look. Identifying closely with our brand name is very important as well.

I've attached images of the product, and the image the branding was inspired from. A color palette based on those images would be nice but is not necessarily required. Please note however that our discs are yellow and not red.

We do not have our box template from our manufacturer yet but the dimensions of the box will be 127x127x74mm

Target Market(s)

We are aiming at a beginner to mid-level power tool user.

Industry/Entity Type

Power Tool

Font styles to use
Serif
Decorative

Colors

Designer to choose colors to be used in the design.

Requirements
Must have
• Our Brand name, Badger Bite must be on the box, preferably in a strong Bold font.
• We would also like our slogan somewhere on the box: "Designed for Strength, Built to Last"
• I've also attached an image showing the number of pieces of each grit sandpaper is in each box. We would like some similar indication on our packaging. Also an indication that these are 8 hole sanding discs is needed as well.
Nice to have
• The packaging may also be used for other sanding products such as sanding belts, sponges, etc as the line expands so versatility is a plus. A vector design is preferred.
• A space on the back of the package for a more detailed product description with a matching font would helpful. The copy hasn't been written yet but the description will around 100 words. Placeholder text would be fine.
Should not have
• Absolutely DO NOT use images from other artists within your design. If this is done you will not win this design contest. I
• Also, please do not use the attached gorilla image in your designs. We have tried to locate the copyright holder to obtain printing rights but haven't been successful.
• Also, please stay away from the aesthetic of the product "Walrus paste". For trademark purposes the design needs to be as distinct from that product logo and packaging as possible.

```html
<!DOCTYPE html>
<html lang="en">
<head>
<meta charset="utf-8">
<title>Badger Bite – Sanding Disc Box Dieline</title>
<link rel="stylesheet" href="https://fonts.googleapis.com/css2?family=Oswald:wght@600&family=Montserrat:wght@400;600;700;800&display=swap">
<style>
  :root {
    --canvas: #ececec;
    --box-black: #0f0e0b;
    --outline: #000000;
    --cut-red: #c1272d;
    --gold: #c89214;
    --white: #ffffff;
    --photo-dark: #1a1a1a;
    --photo-mid: #5a5a5a;
  }
  html, body { margin: 0; padding: 0; overflow: hidden; }
  body { width: 1200px; height: 1100px; background: var(--canvas); }
  .dieline { display: block; width: 1200px; height: 1100px; }
  .panel { fill: var(--box-black); stroke: var(--outline); stroke-width: 4; stroke-linejoin: round; }
  .fold-line { fill: none; stroke: var(--cut-red); stroke-width: 0.8; }
  .gold-band { fill: var(--gold); }
  .disc-outline { fill: none; stroke: var(--white); stroke-width: 2; }
  .disc-hole { fill: none; stroke: var(--white); stroke-width: 2; }
  .brand-name { font-family: "Oswald", sans-serif; font-weight: 600; fill: var(--white); }
  .slogan-small { font-family: "Montserrat", sans-serif; fill: var(--white); }
  .slogan-large { font-family: "Montserrat", sans-serif; fill: var(--white); }
  .slogan-mark { fill: var(--gold); }
  .spec-gold { font-family: "Montserrat", sans-serif; font-weight: 700; fill: var(--gold); }
  .spec-white { font-family: "Montserrat", sans-serif; fill: var(--white); }
  .rule { stroke: var(--white); stroke-width: 1; fill: none; }
  .category-tag { fill: var(--gold); }
  .category-text { font-family: "Montserrat", sans-serif; font-size: 9.5px; fill: var(--white); letter-spacing: 0.3px; }
  .legal-text { font-family: "Montserrat", sans-serif; font-weight: 700; font-size: 7px; fill: var(--white); }
</style>
</head>
<body>
<svg class="dieline" viewBox="0 0 1200 1100" xmlns="http://www.w3.org/2000/svg">
  <defs>
    <linearGradient id="photoTone" x1="0" y1="0" x2="1" y2="0.3">
      <stop offset="0" stop-color="#0f0e0b"/>
      <stop offset="0.55" stop-color="#3a3a3a"/>
      <stop offset="1" stop-color="#6b6b6b"/>
    </linearGradient>
  </defs>

  <!-- Side panel with glue tab and tuck flap -->
  <path class="panel" d="M65 445 L24 452 Q22 453 22 456 L22 598 Q22 602 26 603 L65 610 Z"/>
  <path class="panel" d="M65 437 L65 250 Q65 240 75 240 L125 240 Q137 240 137 252 L137 296 L273 296 L273 252 Q273 240 285 240 L337 240 Q347 240 347 250 L345 437 Z"/>
  <path class="panel" d="M65 437 L343 437 L343 610 L226 610 Q226 590 207 590 Q188 590 188 610 L65 610 Z"/>

  <!-- Back panel -->
  <path class="panel" d="M345 437 L482 367 L482 315 Q482 303 494 303 L613 303 Q623 303 623 313 L622 437 Z"/>
  <rect class="panel" x="343" y="437" width="279" height="173"/>
  <path class="gold-band" d="M343 610 L621 610 L621 743 L360 743 Z"/>

  <!-- Front panel top -->
  <path class="panel" d="M622 437 L685 302 L685 252 Q685 240 697 240 L820 240 Q832 240 832 252 L832 300 L897 437 Z"/>
  <rect class="panel" x="620" y="437" width="279" height="173"/>

  <!-- Right side panel -->
  <path class="panel" d="M897 437 L897 313 Q897 303 907 303 L1025 303 Q1037 303 1037 315 L1037 365 L1176 437 Z"/>
  <rect class="panel" x="899" y="437" width="277" height="173"/>
  <path class="gold-band" d="M901 610 L1176 610 L1145 743 L903 743 Z"/>

  <!-- Front face and bottom tab -->
  <path class="panel" d="M619 610 L901 610 L901 905 Q901 935 871 935 L650 935 Q619 935 619 905 Z"/>
  <rect x="760" y="610" width="140" height="280" fill="url(#photoTone)" role="img" aria-label="Photograph of a badger looking toward the viewer, dark monochrome"/>

  <!-- Fold and cut guides -->
  <g class="fold-line">
    <path d="M70 437 L1170 437"/>
    <path d="M343 437 L343 610 M620 437 L620 890 M899 437 L899 890"/>
    <path d="M70 605 L70 250 L135 250 L135 300 L275 300 L275 250 L340 250"/>
    <path d="M486 370 L486 310 L618 310 M690 302 L690 248 L828 248 L828 300 M1033 365 L1033 310 L903 310"/>
    <path d="M625 890 L625 905 Q625 930 650 930 L870 930 Q895 930 895 905 L895 890"/>
    <path d="M28 455 L28 598"/>
  </g>

  <!-- Back panel bottom disc graphic -->
  <g class="disc-art">
    <path class="disc-outline" d="M390 743 A105 105 0 0 1 600 743"/>
    <circle class="disc-hole" cx="476" cy="689" r="8"/>
    <circle class="disc-hole" cx="517" cy="690" r="8"/>
    <circle class="disc-hole" cx="446" cy="718" r="8"/>
    <circle class="disc-hole" cx="545" cy="719" r="8"/>
  </g>
  <g class="disc-art">
    <path class="disc-outline" d="M915 743 A105 105 0 0 1 1125 743"/>
    <circle class="disc-hole" cx="1001" cy="689" r="8"/>
    <circle class="disc-hole" cx="1042" cy="690" r="8"/>
    <circle class="disc-hole" cx="971" cy="718" r="8"/>
    <circle class="disc-hole" cx="1070" cy="719" r="8"/>
  </g>

  <!-- Upside-down brand blocks on top-facing panels -->
  <g class="brand-block" transform="rotate(180 478 520)">
    <text class="brand-name" x="430" y="480" font-size="17">BADGER</text>
    <text class="brand-name" x="430" y="500" font-size="21">BITE</text>
    <rect class="slogan-mark" x="408" y="510" width="3" height="10"/>
    <rect class="slogan-mark" x="413" y="510" width="3" height="10"/>
    <text class="slogan-large" x="420" y="520" font-size="14" font-weight="400">DESIGNED FOR</text>
    <text class="slogan-large" x="420" y="540" font-size="19" font-weight="800">STRENGTH</text>
    <text class="slogan-large" x="420" y="560" font-size="17" font-weight="400">BUILT TO LAST</text>
  </g>
  <g class="brand-block" transform="rotate(180 1037 520)">
    <text class="brand-name" x="989" y="480" font-size="17">BADGER</text>
    <text class="brand-name" x="989" y="500" font-size="21">BITE</text>
    <rect class="slogan-mark" x="967" y="510" width="3" height="10"/>
    <rect class="slogan-mark" x="972" y="510" width="3" height="10"/>
    <text class="slogan-large" x="979" y="520" font-size="14" font-weight="400">DESIGNED FOR</text>
    <text class="slogan-large" x="979" y="540" font-size="19" font-weight="800">STRENGTH</text>
    <text class="slogan-large" x="979" y="560" font-size="17" font-weight="400">BUILT TO LAST</text>
  </g>

  <!-- Upside-down spec block on side panel -->
  <g class="side-spec" transform="rotate(180 208 505)">
    <circle class="disc-outline" cx="207" cy="465" r="24"/>
    <g class="disc-hole" stroke-width="1.2">
      <circle cx="207" cy="453" r="2.5"/><circle cx="216" cy="457" r="2.5"/>
      <circle cx="219" cy="466" r="2.5"/><circle cx="215" cy="475" r="2.5"/>
      <circle cx="207" cy="478" r="2.5"/><circle cx="198" cy="475" r="2.5"/>
      <circle cx="195" cy="466" r="2.5"/><circle cx="199" cy="457" r="2.5"/>
    </g>
    <text class="legal-text" x="207" y="511" text-anchor="middle">4PK  |  8 HOLE  |  5# (125) 320 GRIT</text>
    <rect class="category-tag" x="126" y="519" width="165" height="14"/>
    <text class="category-text" x="208" y="530" text-anchor="middle" font-size="8.5">RANDOM ORBITAL SANDER PADS</text>
    <text class="legal-text" x="208" y="544" text-anchor="middle">HOOK &amp; LOOP</text>
    <path class="rule" d="M104 560 L108 548 L308 548 L312 560"/>
  </g>

  <!-- Upside-down origin note on front top panel -->
  <g class="origin-note" transform="rotate(180 733 453)">
    <text class="legal-text" x="722" y="450">Made in USA</text>
    <text class="legal-text" x="722" y="459">00-0000</text>
  </g>

  <!-- Front face content -->
  <g class="front-face">
    <text class="brand-name" x="628" y="645" font-size="27" letter-spacing="0.5">BADGER</text>
    <text class="brand-name" x="628" y="690" font-size="44">BITE</text>
    <path class="rule" d="M650 692 L650 696 L712 696"/>
    <text class="slogan-small" x="662" y="704" font-size="6.5" font-weight="400"><tspan class="slogan-mark" fill="#c89214">‖</tspan> DESIGNED FOR</text>
    <text class="slogan-small" x="662" y="711" font-size="7" font-weight="800">STRENGTH</text>
    <text class="slogan-small" x="662" y="718" font-size="6.5" font-weight="400">BUILT TO LAST</text>

    <circle class="disc-outline" cx="758" cy="655" r="37"/>
    <g class="disc-hole" stroke-width="1.5">
      <circle cx="753" cy="639" r="3"/><circle cx="767" cy="640" r="3"/>
      <circle cx="776" cy="652" r="3"/><circle cx="775" cy="666" r="3"/>
      <circle cx="765" cy="675" r="3"/><circle cx="751" cy="675" r="3"/>
      <circle cx="741" cy="663" r="3"/><circle cx="742" cy="648" r="3"/>
    </g>
    <path class="rule" d="M758 692 L758 765 L646 765 L640 755"/>

    <text class="spec-gold" x="646" y="758" font-size="17">4 PK</text>
    <text class="spec-gold" x="647" y="778" font-size="9.5">8 HOLE</text>
    <text class="spec-white" x="649" y="798" font-size="12" font-weight="700">5# (125) 320 GRIT</text>
    <path class="rule" d="M646 805 L788 805"/>
    <text class="spec-white" x="649" y="817" font-size="10" font-weight="400">HOOK &amp; LOOP</text>
    <text class="spec-white" x="649" y="837" font-size="7" font-weight="400">Ideal for timber and general use</text>
    <rect class="category-tag" x="644" y="847" width="149" height="28"/>
    <text class="category-text" x="648" y="859">RANDOM ORBITAL</text>
    <text class="category-text" x="648" y="870">SANDER PADS</text>
  </g>
</svg>
</body>
</html>
```